sticker of engine oil bottle

Dear Designers
i want to design new sticker for my bottle engine oil brand
i want the sticker creative and get harmonic with the bottle color one Blue and another color Red
my brand name is (Tinrel) as attached logo and pictures and i will attached pictures you can take ideas from it
The Shape of Plastic bottle i used is the first bottle attached in blue color Tinrel 20W50 and in red color tinrel 5W30
i want new creative design calms colors and designs
and not copy paste from another design

Target Market(s)

car care and engine oil service centers

Requirements
Must have
• companies approvals and certificates
Nice to have
• new idea
Should not have
• copy past from another design on internet

```html
<!DOCTYPE html>
<html lang="en">
<head>
<meta charset="utf-8">
<title>Tinrel 5W30 Lubricants Label</title>
<link href="https://fonts.googleapis.com/css2?family=Montserrat:wght@400;600;700;800;900&display=swap" rel="stylesheet">
<style>
  :root {
    --canvas-bg: #a9a9a9;
    --label-red: #c0141f;
    --label-red-deep: #8e0a12;
    --gold-light: #fdf4d6;
    --gold: #e8b832;
    --gold-deep: #b98512;
    --silver: #d9d9d9;
    --silver-dark: #6d6d6d;
    --title-yellow: #ffe000;
    --text-white: #ffffff;
    --text-soft: #f1d7d9;
    --brand-blue: #1f4d9a;
  }
  html, body {
    margin: 0;
    padding: 0;
    width: 1200px;
    height: 2767px;
    overflow: hidden;
    background: var(--canvas-bg);
  }
  .canvas {
    position: relative;
    width: 1200px;
    height: 2767px;
  }
  .label {
    position: absolute;
    left: 97px;
    top: 708px;
    width: 1005px;
    height: 1350px;
    font-family: 'Montserrat', sans-serif;
  }
  .brand-name { font-weight: 800; fill: var(--brand-blue); font-size: 44px; }
  .product-title { font-weight: 800; fill: var(--title-yellow); font-size: 50px; letter-spacing: 1px; }
  .product-line { font-weight: 700; fill: var(--text-white); font-size: 16.5px; }
  .grade { font-weight: 900; fill: var(--text-white); font-size: 112px; paint-order: stroke; stroke: var(--label-red-deep); stroke-width: 4px; }
  .spec-heading { font-weight: 800; fill: var(--title-yellow); font-size: 15.5px; }
  .spec-list { font-weight: 400; fill: var(--text-soft); font-size: 15px; }
  .spec-standard { font-weight: 700; fill: var(--text-white); font-size: 15px; }
  .base-type { font-weight: 700; fill: var(--title-yellow); font-size: 15px; }
  .volume { font-weight: 900; fill: var(--label-red); font-size: 92px; paint-order: stroke; stroke: var(--text-white); stroke-width: 8px; }
</style>
</head>
<body>
<div class="canvas">
  <svg class="label" viewBox="225 1780 670 900" xmlns="http://www.w3.org/2000/svg">
    <defs>
      <clipPath id="label-shape">
        <path d="M232 1840 Q232 1795 285 1790 C400 1785 520 1810 590 1840 L870 2540 Q895 2600 880 2630 C700 2645 450 2675 300 2665 Q265 2660 262 2620 Z"/>
      </clipPath>
      <linearGradient id="red-fill" x1="0" y1="0" x2="1" y2="1">
        <stop offset="0" stop-color="var(--label-red)"/>
        <stop offset="0.6" stop-color="#a90f19"/>
        <stop offset="1" stop-color="var(--label-red-deep)"/>
      </linearGradient>
      <radialGradient id="red-glow" cx="0.72" cy="0.52" r="0.25">
        <stop offset="0" stop-color="#e7a4a8" stop-opacity="0.8"/>
        <stop offset="1" stop-color="#e7a4a8" stop-opacity="0"/>
      </radialGradient>
      <linearGradient id="gold-top" x1="0" y1="0" x2="1" y2="1">
        <stop offset="0" stop-color="var(--gold-light)"/>
        <stop offset="0.5" stop-color="#f4e2a6"/>
        <stop offset="1" stop-color="var(--gold)"/>
      </linearGradient>
      <linearGradient id="gold-bottom" x1="0" y1="1" x2="1" y2="0">
        <stop offset="0" stop-color="var(--gold-deep)"/>
        <stop offset="0.45" stop-color="var(--gold)"/>
        <stop offset="0.8" stop-color="#fbe58a"/>
        <stop offset="1" stop-color="var(--gold-deep)"/>
      </linearGradient>
      <linearGradient id="silver-band" x1="0" y1="0" x2="1" y2="0">
        <stop offset="0" stop-color="var(--silver-dark)"/>
        <stop offset="0.5" stop-color="#ffffff"/>
        <stop offset="1" stop-color="var(--silver)"/>
      </linearGradient>
    </defs>

    <g clip-path="url(#label-shape)">
      <rect class="label-base" x="220" y="1780" width="680" height="900" fill="url(#red-fill)"/>
      <rect class="label-glow" x="220" y="1780" width="680" height="900" fill="url(#red-glow)"/>
      <!-- top gold cap -->
      <path class="top-cap" d="M220 1780 L620 1780 L600 1845 C480 1870 320 1930 230 1965 L220 1965 Z" fill="url(#gold-top)"/>
      <path class="top-band" d="M225 1968 C330 1925 470 1870 605 1842 L608 1856 C470 1885 335 1940 228 1985 Z" fill="url(#silver-band)"/>
      <!-- bottom gold sweep -->
      <path class="bottom-sweep" d="M330 2680 C420 2560 620 2440 900 2390 L900 2680 Z" fill="url(#gold-bottom)"/>
      <path class="bottom-band" d="M315 2680 C405 2555 610 2430 900 2378 L900 2392 C620 2445 425 2565 340 2680 Z" fill="url(#silver-band)"/>
    </g>

    <text class="brand-name" x="318" y="1888">Tinrel</text>

    <text class="product-title" x="300" y="2030">LUBRICANTS</text>
    <text class="product-line" x="300" y="2130">HIGH FULL EFFICIENT PETROL ENGINE OIL</text>
    <text class="product-line" x="300" y="2155">HIGH PERFORMANCE PETROL ENGINE OIL</text>

    <text class="grade" x="298" y="2278">5W30</text>

    <text class="spec-heading" x="300" y="2342">MEETS THE REQUIREMENTS OF:</text>
    <text class="spec-list" x="300" y="2368">KR 229.1,&#160;&#160;&#160;NAV M 271</text>
    <text class="spec-list" x="300" y="2393">DTKR 15B110,&#160;&#160;&#160;ALDEN C4</text>
    <text class="spec-list" x="300" y="2418">VERDA VDS,&#160;&#160;&#160;GRANLIFT TO-2</text>

    <text class="spec-standard" x="300" y="2463">API SL/CF&#160;&#160;&#160;&#160;ACEA A3/B4</text>
    <text class="base-type" x="300" y="2488">MINERAL</text>

    <text class="volume" x="655" y="2592">5L</text>
  </svg>
</div>
</body>
</html>
```